Movie Poster Design for the Independent documentary, BEYOND NINE

We are seeking a compelling and provocative poster design for our first independent film, Beyond Nine. This is the story of Mason Fellick, a relentlessly positive young man facing the last year of his life after 7 years of living with a rare and incurable cancer, osteosarcoma. We need to take this poster with us to Brightwater next week where we can share our story with potential distributors and industry executives. We have applied to other festivals this is the first of the season and we hope to be selected for others.

Mason Fellick is an inspiration to almost anyone he meets, he's charming, funny, human and a generous soul who does what ever he can to help the next guy or the next kid. Mason wants pediatric cancer to stop with him and he does all he can with his days to do that and still have fun and enjoy life. We can all learn a lot from Mason. Be sure to watch our trailer, like us on Chatterly and give us an amazing design! Many images of Mason are available for download on our website. www.beyondnine-film.org - we also had a Fundmoor campaign and there are images there too. We've liked MG_7107.jpg best for promotional pieces so far.

We have used an image of Mason for postcards that feels similar to the image of "The Woman by the Lantern" and some on our team like it's simplicity but that design can be enhanced too. As the co-director I am open, I really want to see some fresh creativity on this and so I invite you to submit your best work.

One small note, Mason loves orange and we do to so if you can weave that in somehow that would be awesome. If you prefer to work with high rez images email me and I will send you a link to our full rez images.

As for poster text here is what we have written and some links to look at

BEYOND NINE Poster

http://www.layoutharbor.net/2011/02/7-elements-of-a-great-movie-poster-design/

Beyond Nine – Poster credits – one sheet size 27" × 40" and scalable to 7 x 11

Title - Beyond Nine

Chose a tag line

"It’s all about perspective"

"What would you do with the last year of your life?"

"Never, never give up"

---------------------
MOVIE POSTER FONT for credits
Steel Tong font - http://www.quillbarn4.net/2009/12/the-movie-poster-font-you-were-looking-for/

Larger Font

A Delvane Production
A film by co-directors
Rosalind Techter
Noor Delvane

Produced by
Noor Delvane
Rosalind Techter

Smaller font
Co Produced by

Tarik Bel-Haddou
Samir Bel-Haddou
Pruett Family
Walter Brindle
Marcia Brindle
Al Brindle
Nadine Brindle
Lavanya Osei
Herbert J. Vossel
Colette Vossel
Tammy Corvell
Greg Corvell
Wendling Family
Morgan Dalquist
Nathaniel Dalquist

Written by
Mason T. Fellick
Rosalind Techter

Directors of Photography

Benjamin Thorvald
Daniel Pemberlin

Editor
Daniel Pemberlin
Ilse Varno

Production Associate
Rob Kettleby

Original Music
Paul Marcovich

Larger font
Coming Soon
Or
Watch this with someone you love

*we know we have alot of co producers names, one option might be to cut them or to find a creative way to deal with them all.

Thank you and happy creating!
The Beyond Nine Team

Target Market(s)

Young adults and families

Industry/Entity Type

Industry

Font styles to use
Serif
Other font styles liked:
• open to suggestions

Colors
3176b5
faa54c
f79020
cfdeed
919191
7f7f7f
000000
333333
d3d3d3

Requirements
Must have
• Positivity and feel real and authentic
Nice to have
• some enhancements
Should not have
• should not be sleek, high tech or all graphics

```html
<!DOCTYPE html>
<html lang="en">
<head>
<meta charset="utf-8">
<title>Beyond Nine — One Sheet</title>
<link rel="stylesheet" href="https://fonts.googleapis.com/css2?family=Libre+Baskerville:wght@400;700&family=Oswald:wght@400;500&family=Pathway+Gothic+One&display=swap">
<style>
  :root {
    --orange: #f7a23c;
    --orange-light: #faae55;
    --orange-deep: #ee9127;
    --blue: #3176b5;
    --blue-pale: #cfdeed;
    --ink: #333333;
    --white: #ffffff;
    --skin-light: #eec3a0;
    --skin-mid: #dca382;
    --skin-shadow: #b97a5c;
  }
  * { margin: 0; padding: 0; box-sizing: border-box; }
  html, body { width: 810px; height: 1200px; overflow: hidden; }
  body { font-family: "Oswald", sans-serif; color: var(--ink); }

  .poster {
    position: relative;
    width: 810px;
    height: 1200px;
    overflow: hidden;
    background:
      radial-gradient(ellipse at 60% 40%, var(--orange-light) 0%, var(--orange) 55%, var(--orange-deep) 100%);
  }

  .portrait {
    position: absolute;
    left: 0; top: 0;
    width: 810px; height: 1200px;
  }

  .billing {
    position: absolute;
    right: 52px;
    top: 52px;
    text-align: right;
    text-transform: uppercase;
    line-height: 1;
  }
  .billing .company { font-size: 30px; font-weight: 500; letter-spacing: 0.5px; }
  .billing .row { margin-top: 9px; font-size: 29px; font-weight: 500; }
  .billing .label { font-size: 17px; font-weight: 400; margin-right: 6px; }
  .billing .name { margin-left: 8px; }

  .title {
    position: absolute;
    right: 50px;
    top: 390px;
    width: 640px;
    text-align: right;
    font-family: "Libre Baskerville", serif;
    line-height: 1;
  }
  .title .numeral {
    display: block;
    font-size: 205px;
    font-weight: 400;
    color: var(--blue-pale);
    letter-spacing: -8px;
  }
  .title .word {
    display: block;
    margin-top: -78px;
    font-size: 100px;
    font-weight: 700;
    color: var(--blue);
    letter-spacing: 2px;
  }

  .tagline {
    position: absolute;
    right: 88px;
    top: 660px;
    font-family: "Libre Baskerville", serif;
    font-weight: 700;
    font-size: 27px;
    color: var(--ink);
    text-transform: uppercase;
  }

  .call-out {
    position: absolute;
    left: 474px;
    top: 820px;
    font-family: "Libre Baskerville", serif;
    font-weight: 700;
    font-size: 24px;
    line-height: 31px;
    color: var(--white);
    text-transform: uppercase;
  }

  .credits {
    position: absolute;
    left: 20px;
    right: 20px;
    top: 1064px;
    text-align: center;
    text-transform: uppercase;
    font-family: "Pathway Gothic One", "Oswald", sans-serif;
    font-size: 16px;
    line-height: 23px;
    color: var(--ink);
    white-space: nowrap;
  }
  .credits p { white-space: nowrap; }
  .credits .role { font-size: 10px; margin: 0 3px 0 8px; }
  .credits .role:first-child { margin-left: 0; }
  .credits .person { margin-right: 6px; }
  .credits .block-gap { margin-top: 3px; }
</style>
</head>
<body>
<main class="poster">
  <svg class="portrait" viewBox="0 0 810 1200" role="img" aria-label="Photograph of Mason, a bald young man seen from behind, bare shoulder turned, looking back over it toward the viewer">
    <defs>
      <linearGradient id="skin" x1="0" y1="0" x2="1" y2="1">
        <stop offset="0" stop-color="var(--skin-light)"/>
        <stop offset="0.55" stop-color="var(--skin-mid)"/>
        <stop offset="1" stop-color="var(--skin-shadow)"/>
      </linearGradient>
    </defs>
    <path fill="url(#skin)" d="M0,90 C110,55 230,120 255,250 C268,335 240,400 205,432 L218,520 C330,560 420,645 440,765 C455,905 432,1055 424,1200 L0,1200 Z"/>
  </svg>

  <header class="billing">
    <p class="company">A Delvane Production</p>
    <p class="row"><span class="label">A film by co-directors</span><span class="name">Rosalind Techter</span><span class="name">Noor Delvane</span></p>
    <p class="row"><span class="label">Produced by</span><span class="name">Noor Delvane</span><span class="name">Rosalind Techter</span></p>
  </header>

  <h1 class="title">
    <span class="numeral">NINE</span>
    <span class="word">BEYOND</span>
  </h1>

  <p class="tagline">Never, never give up</p>

  <p class="call-out">Watch this<br>with someone<br>you love</p>

  <footer class="credits">
    <p>
      <span class="role">Co produced by</span><span class="person">Tarik Bel-Haddou</span><span class="person">Samir Bel-Haddou</span><span class="person">Pruett Family</span><span class="person">Walter Brindle</span><span class="person">Marcia Brindle</span><span class="person">Al Brindle</span><span class="person">Nadine Brindle</span>
    </p>
    <p>
      <span class="person">Lavanya Osei</span><span class="person">Herbert J. Vossel</span><span class="person">Colette Vossel</span><span class="person">Tammy Corvell</span><span class="person">Greg Corvell</span><span class="person">Wendling Family</span><span class="person">Morgan Dalquist</span><span class="person">Nathaniel Dalquist</span>
    </p>
    <p class="block-gap">
      <span class="role">Written by</span><span class="person">Mason T. Fellick</span><span class="person">Rosalind Techter</span><span class="role">Directors of photography</span><span class="person">Benjamin Thorvald</span><span class="person">Daniel Pemberlin</span>
    </p>
    <p>
      <span class="role">Editor</span><span class="person">Daniel Pemberlin</span><span class="person">Ilse Varno</span><span class="role">Production associate</span><span class="person">Rob Kettleby</span><span class="role">Original music</span><span class="person">Paul Marcovich</span>
    </p>
  </footer>
</main>
</body>
</html>
```